Popular Australian based wellbeing and high performance podcast needs a design

I need a new, fresh design for my Keep Rising Daily podcast image. This podcast helps and enables its listeners to do their life even better by enhancing their wellbeing, mindset, happiness and leadership. I would love to see designs that include the colour blue. The final design should communicate optimism, hope, approachability and credibility.

Target Market(s)

Target is teenagers to adults wanting to enhance their wellbeing, mindset and happiness.

Font styles to use
Other font styles liked:
• Proba Pro

Colors
33a6d7
0592cd
ffffff

Requirements
Must have
• Must include: Keep Rising Daily podcast
Nice to have
• Could include: with Mick Talvero.

```html
<!DOCTYPE html>
<html lang="en">
<head>
<meta charset="utf-8">
<title>Keep Rising Daily – Podcast Cover</title>
<link rel="stylesheet" href="https://fonts.googleapis.com/css2?family=Arimo:wght@400&display=swap">
<style>
  :root {
    --page-bg: #ececec;
    --blue-top: #0592cd;
    --blue-mid: #0a6fae;
    --blue-bottom: #003470;
    --ink-white: #ffffff;
    --host-tone-light: #c9b8ad;
    --host-tone-mid: #a99b93;
    --host-tone-dark: #2a2f3a;
  }
  html, body {
    margin: 0;
    padding: 0;
    width: 1195px;
    height: 1200px;
    overflow: hidden;
    background: var(--page-bg);
  }
  .cover {
    position: absolute;
    left: 47px;
    top: 50px;
    width: 1100px;
    height: 1100px;
    overflow: hidden;
    background: linear-gradient(180deg, var(--blue-top) 0%, var(--blue-mid) 45%, var(--blue-bottom) 100%);
    font-family: "Arimo", Arial, Helvetica, sans-serif;
    color: var(--ink-white);
  }
  .host-photo {
    position: absolute;
    left: 0;
    top: 0;
    width: 1100px;
    height: 1100px;
  }
  .host-credit {
    position: absolute;
    left: 0;
    right: 0;
    top: 0;
    text-align: center;
  }
  .host-credit__with {
    position: absolute;
    left: 212px;
    top: 22px;
    font-size: 64px;
    line-height: 1;
    letter-spacing: 1px;
  }
  .host-credit__name {
    position: absolute;
    left: 0;
    right: 0;
    top: 62px;
    font-size: 158px;
    line-height: 1;
    letter-spacing: -2px;
    white-space: nowrap;
  }
  .show-title {
    position: absolute;
    left: 140px;
    top: 612px;
    margin: 0;
    font-weight: 400;
    font-size: 178px;
    line-height: 212px;
    letter-spacing: -5px;
    white-space: nowrap;
    text-shadow: 0 2px 6px rgba(0, 0, 0, 0.25);
  }
  .show-title span { display: block; }
</style>
</head>
<body>
  <main class="cover">
    <svg class="host-photo" viewBox="0 0 1100 1100" role="img" aria-label="Photo of the host, smiling, seated with arms resting on knees, wearing a grey t-shirt">
      <defs>
        <linearGradient id="hostTone" x1="0" y1="0" x2="0" y2="1">
          <stop offset="0" stop-color="var(--host-tone-light)" stop-opacity="0.85"/>
          <stop offset="0.55" stop-color="var(--host-tone-mid)" stop-opacity="0.9"/>
          <stop offset="1" stop-color="var(--host-tone-dark)"/>
        </linearGradient>
      </defs>
      <path d="M84 1100 L84 860 Q110 700 240 640 L320 580 Q330 330 480 300 Q640 290 640 560 L760 620 Q900 690 950 860 L958 1100 Z" fill="url(#hostTone)"/>
    </svg>

    <header class="host-credit">
      <div class="host-credit__with">with</div>
      <div class="host-credit__name">Mick Talvero</div>
    </header>

    <h1 class="show-title">
      <span>Keep Rising</span>
      <span>Daily</span>
    </h1>
  </main>
</body>
</html>
```